Webdesign für Arbeitsschutz
Zielgruppe
Grundlage für ein funktionierendes Beschäftigungssystem ist die Schaffung und der Erhalt sicherer und menschengerechter Arbeitsbedingungen. Ein effizienter Arbeitsschutz und eine wirksame Unfallvermeidung sind hierfür besonders wichtig, vor allem auch im Hinblick auf die Herausforderungen einer durch digitalen Wandel immer schnelleren und anspruchsvolleren Arbeitswelt. Sicherheit und Gesundheit bei der Arbeit sind deshalb wichtige Arbeitsschwerpunkte im Landesamt für Betriebe und Sozialwesen. Ziel ist es, die Beschäftigten wirksam vor Gefahren und gesundheitlichen Schädigungen zu schützen. Verlässliche gesetzliche Grundlagen und rechtssichere Rahmenbedingungen für alle Unternehmen sind dafür unerlässlich.
Das wichtigste Grundlagengesetz für den betrieblichen Arbeitsschutz ist das Arbeitsschutzgesetz (ArbSchG). Es verpflichtet den Arbeitgeber, Gesundheitsgefährdungen am Arbeitsplatz zu beurteilen und über notwendige Schutzmaßnahmen zu entscheiden. Der Arbeitgeber hat für eine funktionierende Arbeitsschutzorganisation im Betrieb zu sorgen. Dies kann besonders wirksam durch eine nachhaltige Einbindung des Arbeits- und Gesundheitsschutzes in die Strukturen und Abläufe eines Unternehmens erreicht werden.
Aufgabenstellung
Gerne eine helle Seite mit schöner integration des Logo´s in die Homepage
Ich möchte keine exakte Kopie der Internet-Seite haben, aber alle Inhalte die Lemm-Arbeitsschutz anbietet (inkl. Rückrufservice, Anbringen von Referenz-Logos, Navigationsmenü)
Die Gestaltung der Hauptseite mit Farbe sollte bitte mit den vorhandenen Logo harmonieren. Die Aufteilung wo sich die Bausteine (Rückrufservice etc.) befindet sollte übersichtlich angebracht sein.

```html
<!DOCTYPE html>
<html lang="de">
<head>
<meta charset="utf-8">
<title>Arbeitsschutz &amp; Gesundheit Süd GmbH</title>
<link href="https://fonts.googleapis.com/css2?family=Roboto+Condensed:wght@300;400;700&family=Roboto:wght@400;700&display=swap" rel="stylesheet">
<style>
:root{
  --teal:#0e6c7d;
  --teal-dark:#0b5f6e;
  --teal-light:#c9e3e9;
  --text:#555;
  --grey-bar:#cfcfcf;
  --white:#fff;
}
*{box-sizing:border-box;margin:0;padding:0}
html,body{width:1200px;height:2695px;overflow:hidden;background:var(--white)}
body{font-family:"Roboto Condensed",sans-serif;color:var(--text);position:relative}
.sec{position:absolute;left:0;width:1200px}
.band{background:linear-gradient(90deg,var(--teal) 0%,var(--teal) 45%,#3f8d9b 75%,var(--teal-light) 100%)}
.btn{display:inline-flex;align-items:center;justify-content:center;background:var(--teal);color:var(--white);border-radius:22px;font-family:"Roboto",sans-serif;font-size:16px}
.h2{font-weight:400;font-size:24px;color:var(--teal)}
.bars{display:flex;gap:24px;margin-top:12px}
.bars span{display:block;width:79px;height:4px;background:var(--grey-bar)}
.bars span+span{background:var(--teal)}
.copy{font-size:12px;line-height:15px;color:#666}

/* hero */
.hero{top:0;height:435px;overflow:hidden}
.hero-photo{position:absolute;inset:0;background:linear-gradient(90deg,#eef0f2 0%,#dfe3e6 40%,#d8b77a 60%,#f1c232 72%,#6b6f72 90%,#3e4346 100%)}
.topbar{position:absolute;top:0;left:0;width:1200px;height:132px;background:rgba(255,255,255,.85)}
.logo-box{position:absolute;left:94px;top:0;width:220px;height:173px;background:var(--white);box-shadow:0 2px 6px rgba(0,0,0,.25);display:flex;flex-direction:column;align-items:center;justify-content:center;gap:10px;text-align:center}
.logo-box i{width:26px;height:26px;background:var(--teal)}
.logo-box p{color:var(--teal);font-family:"Roboto",sans-serif;font-size:11.5px;line-height:14px}
.contact{position:absolute;top:14px;display:flex;align-items:center;gap:8px;font-size:10px;line-height:12px;color:#555}
.contact b{width:30px;height:30px;border-radius:50%;background:#e4e4e4;display:flex;align-items:center;justify-content:center;font-weight:700;color:#777;font-size:16px}
.nav{position:absolute;top:76px;left:362px;display:flex;gap:21px;font-size:16px;color:#444;align-items:center}
.hero-title{position:absolute;left:94px;top:206px;font-size:31px;font-weight:400;color:var(--teal);line-height:36px}
.hero .btn{position:absolute;left:94px;top:293px;width:211px;height:41px;font-size:18px}
.dots{position:absolute;left:575px;top:410px;display:flex;gap:6px}
.dots i{width:10px;height:10px;background:#999}
.dots i.on{background:#1a9ad6}

/* intro */
.intro{top:435px;height:298px;color:var(--white);text-align:center}
.intro h1{font-size:23px;margin-top:40px}
.intro p{width:1010px;margin:26px auto 0;font-family:"Roboto",sans-serif;font-weight:700;font-size:11px;line-height:22.5px}

/* safety */
.safety{top:733px;height:334px}
.safety .h2{position:absolute;left:95px;top:22px}
.safety .bars{position:absolute;left:95px;top:48px}
.safety .lead{position:absolute;left:92px;top:86px;width:315px}
.safety .lead p+p{margin-top:15px}
.ticks{position:absolute;left:451px;top:87px;list-style:none;font-size:12px;color:#666}
.ticks li{height:22.5px;display:flex;gap:6px;align-items:flex-start}
.ticks svg{margin-top:3px}
.helmet{position:absolute;left:638px;top:-50px;width:525px;height:345px;border-radius:40% 40% 20% 20%;background:radial-gradient(ellipse at 40% 45%,#f6c21c 0%,#e8a912 35%,#2d3f3f 62%,#bdbdbd 78%,rgba(255,255,255,0) 92%)}
.safety .btn{position:absolute;left:94px;top:257px;width:170px;height:41px}

/* icons */
.icons{top:1067px;height:442px;color:var(--white);text-align:center}
.icons h2{font-size:23px;margin-top:39px}
.icons .sub{font-family:"Roboto",sans-serif;font-weight:700;font-size:11px;line-height:23px;margin-top:14px}
.cols{position:absolute;left:94px;top:167px;display:flex;width:1012px}
.col{width:168.6px;display:flex;flex-direction:column;align-items:center}
.col .ic{width:56px;height:56px;border-radius:50%;background:var(--white);display:flex;align-items:center;justify-content:center}
.col h3{font-size:15px;line-height:15px;margin-top:17px}
.col p{font-size:12px;line-height:15.5px;height:76px}
.col .ob{margin-top:4px;width:118px;height:27px;border:1.5px solid var(--white);border-radius:14px;font-size:10px;line-height:10px;display:flex;align-items:center;justify-content:center}

/* info */
.info{top:1509px;height:385px}
.info .block{position:absolute;top:55px;width:380px}
.info .block .copy{margin-top:28px}
.info .block .copy p+p{margin-top:15px}
.info .btn{position:absolute;top:303px;width:170px;height:41px}

/* refs */
.refs{top:1894px;height:272px;text-align:center}
.refs .h2{margin-top:34px}
.refs .bars{justify-content:center}
.logos{position:absolute;left:136px;top:99px;display:flex;gap:26px}
.logos div{width:213px;height:129px;background:var(--white);box-shadow:0 1px 4px rgba(0,0,0,.2);border-bottom:3px solid #ccc;display:flex;align-items:center;justify-content:center;font-family:"Roboto",sans-serif;font-weight:700;font-size:24px;color:#333}
.arrow{position:absolute;top:153px;width:32px;height:46px;background:var(--teal);display:flex;align-items:center;justify-content:center}
.arrow.l{left:0;border-radius:0 23px 23px 0}
.arrow.r{right:0;border-radius:23px 0 0 23px}

/* map */
.map{top:2166px;height:263px;background:linear-gradient(90deg,#ececec 0%,#e6e6e6 74%,#f2e7a0 75%,#9fc8f0 77%,#a8cdf3 100%)}

/* footer */
.footer{top:2429px;height:266px;color:var(--white)}
.f-brand{position:absolute;left:94px;top:28px;width:270px;text-align:center;display:flex;flex-direction:column;align-items:center;gap:14px}
.f-brand i{width:60px;height:60px;border:3px solid var(--white)}
.f-brand p{font-family:"Roboto",sans-serif;font-size:16px;line-height:19px}
.f-col{position:absolute;top:24px;font-size:11px;line-height:13.5px;font-weight:700}
.f-col h4{font-size:20px;font-weight:400;line-height:22px;margin-bottom:4px}
.f-col .wb{display:inline-block;background:var(--white);color:var(--teal);font-weight:400;border-radius:12px;padding:5px 10px;margin:8px 0 0 -3px}
.f-line{position:absolute;left:94px;top:224px;width:1012px;height:1px;background:rgba(255,255,255,.5)}
.f-copy{position:absolute;top:240px;width:1200px;text-align:center;font-size:10px;font-weight:700}
</style>
</head>
<body>

<section class="sec hero">
  <div class="hero-photo" role="img" aria-label="Foto: Hand hält einen gelben Schutzhelm, Werkzeuggürtel im Hintergrund"></div>
  <div class="topbar"></div>
  <div class="logo-box"><i></i><p>Arbeitsschutz &amp; Gesundheit<br>Süd GmbH</p></div>
  <div class="contact" style="left:734px"><b>i</b><span>Hier könnte die Adresse<br>stehen wenn man möchte</span></div>
  <div class="contact" style="left:912px"><b><svg width="14" height="14" viewBox="0 0 24 24"><path fill="#777" d="M6.6 10.8a15 15 0 0 0 6.6 6.6l2.2-2.2c.3-.3.7-.4 1-.2 1.1.4 2.3.6 3.6.6.6 0 1 .4 1 1V20c0 .6-.4 1-1 1A17 17 0 0 1 3 4c0-.6.4-1 1-1h3.5c.6 0 1 .4 1 1 0 1.3.2 2.5.6 3.6.1.3 0 .7-.2 1z"/></svg></b><span>(0) 3412 55 66 77<br><span style="font-size:12px">kontakt@ags-sued.example</span></span></div>
  <nav class="nav">
    <svg width="20" height="18" viewBox="0 0 20 18"><path d="M2 9 10 2l8 7M4 8v9h5v-5h2v5h5V8" fill="none" stroke="#555" stroke-width="1.6"/></svg>
    <span style="margin-left:-13px">Beratung &amp; Betreuung</span><span>Seminare</span><span>E-Learning</span><span>Beauftragtenwesen</span><span>Das Unternehmen</span><span>Kontakt</span>
  </nav>
  <h2 class="hero-title">Mit Sicherheit<br>mehr Sicherheit</h2>
  <a class="btn">mehr Informationen</a>
  <div class="dots"><i></i><i class="on"></i><i></i></div>
</section>

<section class="sec intro band">
  <h1>Effizienter Arbeitsschutz ist ein MUSS!</h1>
  <p>Grundlage für ein funktionierendes Beschäftigungssystem ist die Schaffung und der Erhalt sicherer und menschengerechter Arbeitsbedingungen. Ein effizienter Arbeitsschutz und eine wirksame Unfallvermeidung sind hierfür besonders wichtig, vor allem auch im Hinblick auf die Herausforderungen einer durch digitalen Wandel immer schnelleren und anspruchsvolleren Arbeitswelt. Sicherheit und Gesundheit bei der Arbeit sind deshalb wichtige Arbeitsschwerpunkte im Landesamt für Betriebe und Sozialwesen. Ziel ist es, die Beschäftigten wirksam vor Gefahren und gesundheitlichen Schädigungen zu schützen. Verlässliche gesetzliche Grundlagen und rechtssichere Rahmenbedingungen für alle Unternehmen sind dafür unerlässlich. Das wichtigste Grundlagengesetz für den betrieblichen Arbeitsschutz ist das Arbeitsschutzgesetz (ArbSchG). Es verpflichtet den Arbeitgeber, Gesundheitsgefährdungen am Arbeitsplatz zu beurteilen und über notwendige Schutzmaßnahmen zu entscheiden. Der Arbeitgeber hat für eine funktionierende Arbeitsschutzorganisation im Betrieb zu sorgen. Dies kann besonders wirksam durch eine nachhaltige Einbindung des Arbeits- und Gesundheitsschutzes in die Strukturen und Abläufe eines Unternehmens erreicht werden.</p>
</section>

<section class="sec safety">
  <h2 class="h2">Ihre Sicherheit ist unsere Aufgabe!</h2>
  <div class="bars"><span></span><span></span></div>
  <div class="lead copy">
    <p>Lorem ipsum dolor sit amet, consetetur sadipscing elitr, sed diam nonumy eirmod tempor invidunt ut labore et dolore magna aliquyam erat, sed diam voluptua. Lorem ipsum dolor sit amet, consetetur sadipscing elitr, sed diam nonumy eirmod tempor invidunt ut labore et dolore magna aliquyam erat, sed diam voluptua.</p>
    <p>Lorem ipsum dolor sit amet, consetetur sadipscing elitr, sed diam nonumy eirmod tempor invidunt ut labore et dolore magna aliquyam erat, sed diam voluptua.</p>
  </div>
  <ul class="ticks">
    <li><svg width="10" height="9" viewBox="0 0 10 9"><path d="M1 4.5 4 7.5 9 1" fill="none" stroke="#0e6c7d" stroke-width="2"/></svg>Lorem ipsum dolor sit amet,</li>
    <li><svg width="10" height="9" viewBox="0 0 10 9"><path d="M1 4.5 4 7.5 9 1" fill="none" stroke="#0e6c7d" stroke-width="2"/></svg>Lorem ipsum dolor sit amet,</li>
    <li><svg width="10" height="9" viewBox="0 0 10 9"><path d="M1 4.5 4 7.5 9 1" fill="none" stroke="#0e6c7d" stroke-width="2"/></svg>Lorem ipsum dolor sit amet,</li>
    <li><svg width="10" height="9" viewBox="0 0 10 9"><path d="M1 4.5 4 7.5 9 1" fill="none" stroke="#0e6c7d" stroke-width="2"/></svg>Lorem ipsum dolor sit amet,</li>
    <li><svg width="10" height="9" viewBox="0 0 10 9"><path d="M1 4.5 4 7.5 9 1" fill="none" stroke="#0e6c7d" stroke-width="2"/></svg>Lorem ipsum dolor sit amet,</li>
    <li><svg width="10" height="9" viewBox="0 0 10 9"><path d="M1 4.5 4 7.5 9 1" fill="none" stroke="#0e6c7d" stroke-width="2"/></svg>Lorem ipsum dolor sit amet,</li>
  </ul>
  <div class="helmet" role="img" aria-label="Foto: gelber Schutzhelm mit Gehörschutz und Arbeitshandschuhen"></div>
  <a class="btn">mehr erfahren</a>
</section>

<section class="sec icons band">
  <h2>ICONTEXT</h2>
  <p class="sub">Lorem ipsum dolor sit amet, consetetur sadipscing elitr, sed diam nonumy eirmod tempor invidunt<br>ut labore et dolore magna aliquyam erat, sed diam voluptua.</p>
  <div class="cols">
    <div class="col">
      <div class="ic"><svg width="34" height="26" viewBox="0 0 34 26"><g fill="#0e6c7d"><circle cx="17" cy="7" r="5"/><circle cx="7" cy="9" r="4"/><circle cx="27" cy="9" r="4"/><path d="M8 25a9 9 0 0 1 18 0zM0 24a7 7 0 0 1 10-6 10 10 0 0 0-3 6zM34 24a7 7 0 0 0-10-6 10 10 0 0 1 3 6z"/></g></svg></div>
      <h3>Wir stellen ein</h3><p>Informieren Sie sich über unsere Stellenangebote.</p>
      <span class="ob">Zu den<br>Stellenangeboten</span>
    </div>
    <div class="col">
      <div class="ic"><svg width="28" height="30" viewBox="0 0 28 30"><path fill="#0e6c7d" d="M14 1 26 5v9c0 8-6 13-12 15C8 27 2 22 2 14V5z"/></svg></div>
      <h3>Arbeitsschutz</h3><p>Sicherheit geht vor!<br>Wir betreuen Ihr Unternehmen als externe Fachkraft für Arbeitssicherheit.</p>
      <span class="ob">Mehr zum<br>Arbeisschutz</span>
    </div>
    <div class="col">
      <div class="ic"><svg width="34" height="24" viewBox="0 0 34 24"><path fill="#0e6c7d" d="M17 2 33 9 17 16 1 9zM8 13v6c3 3 15 3 18 0v-6l-9 4z"/></svg></div>
      <h3>Seminare</h3><p>Wir bieten eine Vielzahl von fachspezifischen Seminaren rund um den Arbeitsschutz.</p>
      <span class="ob">Übersicht unserer<br>Seminare</span>
    </div>
    <div class="col">
      <div class="ic"><svg width="30" height="26" viewBox="0 0 30 26"><path d="M3 2h24v16H3zM11 24h8M15 18v6" fill="none" stroke="#0e6c7d" stroke-width="3"/></svg></div>
      <h3>E-Learning</h3><p>Sicherheitsunterweisungen online mit E-Learning - flexibel, unkompliziert und zeitsparend.</p>
      <span class="ob">Mehr über unser<br>eLearning</span>
    </div>
    <div class="col">
      <div class="ic"><svg width="28" height="30" viewBox="0 0 28 30"><path d="M3 3h22v24H3z" fill="none" stroke="#0e6c7d" stroke-width="3"/><path fill="#0e6c7d" d="M8 8h12v4H8zM8 16h12v3H8zM8 22h8v2H8z"/></svg></div>
      <h3>Beauftragtenwesen</h3><p>Übernahme der Beauftragten-Funktionen - von Gefahrstoffen bis hin zum Brandschutz.</p>
      <span class="ob">Mehr zum<br>Beauftragtenwesen</span>
    </div>
    <div class="col">
      <div class="ic"><svg width="26" height="30" viewBox="0 0 26 30"><path d="M9 2h8M10 2v10L2 27h22L16 12V2" fill="none" stroke="#0e6c7d" stroke-width="2.5" stroke-linejoin="round"/><path fill="#0e6c7d" d="M6 20h14l3 6H3z"/></svg></div>
      <h3>ChemPro Gefahrstoff<br>Softwarelösung</h3><p style="font-weight:300">Gefahrstoff-Management, einfach wie nie zuvor! Flexibel und anpassbar an Ihre Prozesse.</p>
      <span class="ob" style="margin-top:-11px">Mehr zu<br>ChemPro</span>
    </div>
  </div>
</section>

<section class="sec info">
  <div class="block" style="left:95px">
    <h2 class="h2">Ein informativer Bereich</h2>
    <div class="bars"><span></span><span></span></div>
    <div class="copy" style="margin-left:-3px">
      <p>Lorem ipsum dolor sit amet, consetetur sadipscing elitr, sed diam nonumy eirmod tempor invidunt ut labore et dolore magna aliquyam erat, sed diam voluptua. At vero eos et accusam et justo duo dolores et ea rebum. Stet clita kasd gubergren, no sea takimata sanctus est Lorem ipsum dolor sit amet. Lorem ipsum dolor sit amet, consetetur sadipscing elitr, sed diam nonumy eirmod tempor invidunt ut labore et dolore</p>
      <p>magna aliquyam erat, sed diam voluptua. At vero eos et accusam et justo duo dolores et ea rebum. Stet clita kasd gubergren, no sea takimata sanctus est Lorem ipsum dolor sit amet.</p>
    </div>
  </div>
  <div class="block" style="left:631px;width:400px">
    <h2 class="h2">Sicherheitsschuhe sind wichtig</h2>
    <div class="bars"><span></span><span></span></div>
    <div class="copy" style="margin-left:-3px">
      <p>Lorem ipsum dolor sit amet, consetetur sadipscing elitr, sed diam nonumy eirmod tempor invidunt ut labore et dolore magna aliquyam erat, sed diam voluptua. At vero eos et accusam et justo duo dolores et ea rebum. Stet clita kasd gubergren, no sea takimata sanctus est Lorem ipsum dolor sit amet. Lorem ipsum dolor sit amet, consetetur sadipscing elitr, sed diam nonumy eirmod tempor invidunt ut labore et dolore</p>
      <p>magna aliquyam erat, sed diam voluptua. At vero eos et accusam et justo duo dolores et ea rebum. Stet clita kasd gubergren, no sea takimata sanctus est Lorem ipsum dolor sit amet.</p>
    </div>
  </div>
  <a class="btn" style="left:94px">mehr erfahren</a>
  <a class="btn" style="left:630px">mehr erfahren</a>
</section>

<section class="sec refs">
  <h2 class="h2">Unsere Referenzen</h2>
  <div class="bars"><span></span><span></span></div>
  <div class="logos"><div>Sonnfrucht</div><div>Reinholt</div><div>Schreibwerk</div><div>Frachtmann</div></div>
  <span class="arrow l"><svg width="10" height="16" viewBox="0 0 10 16"><path d="M8 2 2 8l6 6" fill="none" stroke="#fff" stroke-width="3"/></svg></span>
  <span class="arrow r"><svg width="10" height="16" viewBox="0 0 10 16"><path d="M2 2l6 6-6 6" fill="none" stroke="#fff" stroke-width="3"/></svg></span>
</section>

<section class="sec map" role="img" aria-label="Stadtplan mit Standortmarkierung nahe dem Flussufer"></section>

<footer class="sec footer band">
  <div class="f-brand"><i></i><p>Arbeitsschutz &amp; Gesundheit<br>Süd GmbH</p></div>
  <div class="f-col" style="left:398px">
    <h4>Arbeitsschutz &amp;<br>Gesundheit Süd<br>GmbH</h4>
    <p style="margin-top:24px">Lena Brandt<br>Lindenweg 14<br>80331 Auental<br>Deutschland</p>
    <p style="margin-top:14px">&#9990; (0891) - 24 68 10<br>&nbsp;&nbsp;&nbsp;&nbsp;(0891) - 24 68 11</p>
  </div>
  <div class="f-col" style="left:663px">
    <h4>Menü</h4>
    <p>Beratung &amp; Betreuung<br>Seminare<br>E-Learning<br>Beauftragtenwesen<br>Das Unternehmen</p>
  </div>
  <div class="f-col" style="left:853px">
    <h4 style="font-weight:700;font-size:23px">Kontakt</h4>
    <p>Für Anfragen nutzen Sie bitte unser Kontaktformular</p>
    <span class="wb">Zum Kontaktformular</span>
    <h4 style="font-weight:700;font-size:23px;margin-top:18px">Rückrufformular</h4>
    <p>Sie wünschen einen Rückruf? Dann nutzen Sie unser<br>Rückrufformular.</p>
    <span class="wb">Zum Rückrufformular</span>
  </div>
  <div class="f-line"></div>
  <p class="f-copy">© 2018 Agentur Feldgrün | Impressum | AGB | Links</p>
</footer>

</body>
</html>
```